Redesign responsive website and logo for webshop platform

Redesign our applications old website with a new clean, crisp modern looking style that is responsive.

Our application is a cloud based, free ecommerce platform that lets users set up their own webshops within minutes. (Similar to Mabrook https://mabrook.example/l/sell)

Our old website: http://sv.vendlyx.example/

I need redesigned HTML + CSS for the following three pages:
* Landing Page:
(Old page: http://sv.vendlyx.example/)
I have attached a mockup of a proposed layout/structure for the landing page.
- Pricing comparision/features page
(Old page http://sv.vendlyx.example/t/funktioner)
- Generic "article" page:
(Old page http://sv.vendlyx.example/d/redigerasida)

The pages must responsive using HTML 5/CSS 3 (I prefer Bootstrap 3 if possible).

I also need a redesign of the logotype.

If you have any questions don't hesitate to ask and we will provide whatever is needed to you.

Logo Text

Vendlyx

Coding

Coded - Design and coding required

Number of Pages Required

3 page

Font styles to use
Serif
Sans Serif

```html
<!DOCTYPE html>
<html lang="en">
<head>
<meta charset="utf-8">
<title>Vendlyx — Start a free webshop</title>
<link href="https://fonts.googleapis.com/css2?family=Roboto:wght@300;400;500&family=Roboto+Mono:wght@400&display=swap" rel="stylesheet">
<style>
:root{
  --navy:#0e1f2f;
  --yellow:#fbb92c;
  --ink:#2b2b2b;
  --body:#4a4a4a;
  --muted:#8a8a8a;
  --panel:#f1f1f1;
  --line:#e6e6e6;
  --white:#ffffff;
}
*{box-sizing:border-box;margin:0;padding:0}
html,body{width:916px;height:1200px;overflow:hidden}
body{font-family:"Roboto",Arial,sans-serif;color:var(--ink);background:var(--white);position:relative}
a{color:inherit;text-decoration:none}

/* header */
.site-header{position:absolute;top:0;left:0;width:916px;height:48px;background:var(--navy);z-index:2;box-shadow:0 1px 3px rgba(0,0,0,.3)}
.brand{position:absolute;left:68px;top:13px;font-family:"Roboto Mono",monospace;font-size:17px;color:var(--white);letter-spacing:.5px}
.btn-register,.btn-login{position:absolute;top:9px;height:30px;line-height:30px;font-size:10px;text-align:center;text-transform:uppercase}
.btn-register{left:706px;width:68px;background:var(--yellow);color:var(--navy)}
.btn-login{left:781px;width:68px;border:1px solid var(--white);color:var(--white);line-height:28px}

/* hero */
.hero{position:absolute;top:48px;left:0;width:916px;height:371px}
.hero-copy{position:absolute;left:80px;width:310px;top:126px;text-align:center}
.hero-copy h1{font-weight:400;font-size:24px;color:var(--ink);margin-bottom:10px}
.hero-copy p{font-size:10px;line-height:17px;color:var(--body)}
.btn-outline{display:inline-block;margin-top:12px;width:105px;height:27px;line-height:25px;border:1px solid #cfcfcf;font-size:9px;color:var(--ink)}
.hero-photo{position:absolute;left:470px;top:0;width:446px;height:371px;background:linear-gradient(160deg,#c9d2d6 0%,#9fa9ad 35%,#e6e4df 70%,#cfc7bb 100%)}
.hero-callout{position:absolute;left:470px;top:257px;width:248px;height:114px;background:var(--yellow);padding:27px 25px}
.hero-callout h2{font-weight:400;font-size:14px;line-height:17px;color:var(--navy)}
.learn-more{display:flex;align-items:center;gap:6px;margin-top:12px;font-size:8.5px;color:var(--navy);text-transform:uppercase}

/* how it works */
.how{position:absolute;top:419px;left:0;width:916px;height:383px;background:var(--panel);border-bottom:1px solid var(--line)}
.how h2{position:absolute;top:33px;width:100%;text-align:center;font-weight:400;font-size:16px;color:var(--ink)}
.how-grid{position:absolute;left:69px;top:67px;width:779px;display:grid;grid-template-columns:repeat(3,1fr);gap:1px;background:var(--line)}
.how-card{background:var(--white);height:139px;text-align:center;padding:14px 24px 0}
.how-card svg{display:block;margin:0 auto;height:22px}
.how-card h3{font-weight:400;font-size:13px;margin:7px 0 7px;color:var(--ink)}
.how-card p{font-size:9px;line-height:17.6px;color:var(--body);text-align:justify;text-align-last:center}
.how-card.is-active{background:var(--navy)}
.how-card.is-active h3,.how-card.is-active p{color:var(--white);font-weight:500}
.how-card.is-active h3{font-weight:400}

/* features */
.features{position:absolute;top:802px;left:0;width:916px;height:180px}
.feature{position:absolute;top:33px;width:255px}
.feature svg{position:absolute;left:0;top:0}
.feature-body{position:absolute;left:55px;top:0;width:200px}
.feature h3{font-weight:400;font-size:11.5px;color:var(--ink);margin-bottom:4px}
.feature p{font-size:9.5px;line-height:17px;color:var(--muted);text-align:justify}
.feature a{display:block;margin-top:3px;font-size:9.5px;color:var(--ink)}
.dots{position:absolute;top:149px;left:450px;display:flex;gap:4px}
.dots span{width:6px;height:6px;border-radius:50%;border:1px solid var(--navy)}
.dots span.on{background:var(--navy)}

/* newsletter */
.newsletter{position:absolute;top:982px;left:0;width:916px;height:56px;background:var(--yellow);font-size:8.5px;letter-spacing:1.6px;color:var(--navy);text-transform:uppercase}
.newsletter-label{position:absolute;left:68px;top:23px;font-weight:500}
.newsletter-field{position:absolute;left:264px;top:20px;width:243px;height:16px;border-bottom:1px solid rgba(14,31,47,.35);font-size:8px;letter-spacing:.3px;padding-top:3px;color:#6a5320}
.newsletter-field svg{position:absolute;right:2px;top:5px}
.follow{position:absolute;right:68px;top:23px;font-weight:500;display:flex;gap:6px;align-items:center}
.follow i{width:8px;height:8px;background:var(--navy);display:inline-block}

/* footer */
.site-footer{position:absolute;top:1038px;left:0;width:916px;height:162px;background:var(--navy);color:var(--white)}
.footer-brand{position:absolute;top:38px;width:100%;text-align:center;font-family:"Roboto Mono",monospace;font-size:22px}
.social{position:absolute;top:78px;left:404px;display:flex;gap:12px}
.social span{width:28px;height:28px;border-radius:50%;background:#1a2c3d}
.copyright{position:absolute;left:68px;top:140px;font-size:10px}
.legal{position:absolute;right:68px;top:140px;font-size:10px;display:flex;gap:12px}
</style>
</head>
<body>

<header class="site-header">
  <div class="brand">Vendlyx</div>
  <a class="btn-register" href="#">Register</a>
  <a class="btn-login" href="#">Login</a>
</header>

<section class="hero">
  <div class="hero-copy">
    <h1>Start a free websshop</h1>
    <p>Vendlyx is a service that allows you to launch a complete online store. The service is free and has everything needed to get you started with your business and sell products online.</p>
    <a class="btn-outline" href="#">Create a webshop</a>
  </div>
  <div class="hero-photo" role="img" aria-label="Photo of a person working at a laptop in a bright office, with a laptop showing the webshop on a table"></div>
  <div class="hero-callout">
    <h2>Lorem Ipsum dolor de consectetuer adipiscing eli</h2>
    <a class="learn-more" href="#">
      <svg width="17" height="17" viewBox="0 0 17 17"><circle cx="8.5" cy="8.5" r="7.8" fill="none" stroke="#0e1f2f" stroke-width="1"/><path d="M7.5 6l2.5 2.5L7.5 11" fill="none" stroke="#0e1f2f" stroke-width="1"/></svg>
      Learn more
    </a>
  </div>
</section>

<section class="how">
  <h2>How it works</h2>
  <div class="how-grid">
    <div class="how-card">
      <svg viewBox="0 0 22 22" width="22"><circle cx="11" cy="11" r="9" fill="none" stroke="#8a8a8a" stroke-width="1.4"/><path d="M11 5.5V11h4" fill="none" stroke="#8a8a8a" stroke-width="1.4"/></svg>
      <h3>Get started in 5 minutes</h3>
      <p>Starting an E-cart with Vendlyx takes no more than 5 minutes. Create an account to get started. Nothing needs to be installed on your computer.</p>
    </div>
    <div class="how-card">
      <svg viewBox="0 0 22 22" width="22"><circle cx="11" cy="11" r="9.5" fill="#9a9a9a"/><path d="M5 7c3 0 3 3 5 3s1 4 3 4-1 5-1 5M14 3c0 3 3 3 5 4" fill="none" stroke="#fff" stroke-width="1.2"/></svg>
      <h3>Create a free online store</h3>
      <p>Starting an E-cart with Vendlyx takes no more than 5 minutes. Create an account to get started. Nothing needs to be installed on your computer.</p>
    </div>
    <div class="how-card">
      <svg viewBox="0 0 22 22" width="22"><rect x="1" y="1" width="8.5" height="8" fill="none" stroke="#8a8a8a" stroke-width="1.3"/><rect x="12.5" y="1" width="8.5" height="8" fill="none" stroke="#8a8a8a" stroke-width="1.3"/><path d="M1 14h20M1 19h20" stroke="#8a8a8a" stroke-width="1.6"/></svg>
      <h3>Intuitive user interface</h3>
      <p>Starting an E-cart with Vendlyx takes no more than 5 minutes. Create an account to get started. Nothing needs to be installed on your computer.</p>
    </div>
    <div class="how-card">
      <svg viewBox="0 0 22 22" width="22"><circle cx="9" cy="9" r="7" fill="none" stroke="#8a8a8a" stroke-width="1.3"/><path d="M14 14l7 7" stroke="#8a8a8a" stroke-width="1.5"/></svg>
      <h3>Search engine optimized</h3>
      <p>Starting an E-cart with Vendlyx takes no more than 5 minutes. Create an account to get started. Nothing needs to be installed on your computer.</p>
    </div>
    <div class="how-card is-active">
      <svg viewBox="0 0 22 22" width="22"><path d="M3 19l1.5-5L16 2.5l3.5 3.5L8 17.5z M13.5 5l3.5 3.5 M4.5 14l3.5 3.5" fill="none" stroke="#fbb92c" stroke-width="1.3"/></svg>
      <h3>Design your shop</h3>
      <p>Starting an E-cart with Vendlyx takes no more than 5 minutes. Create an account to get started. Nothing needs to be installed on your computer.</p>
    </div>
    <div class="how-card">
      <svg viewBox="0 0 22 22" width="22"><path d="M1 1v20h20 M5 18V5 M8.5 18V10 M12 18V8 M15.5 18V12 M19 18V14" fill="none" stroke="#8a8a8a" stroke-width="1.3"/></svg>
      <h3>Smart Dashboard</h3>
      <p>Starting an E-cart with Vendlyx takes no more than 5 minutes. Create an account to get started. Nothing needs to be installed on your computer.</p>
    </div>
  </div>
</section>

<section class="features">
  <div class="feature" style="left:68px">
    <svg width="44" height="30" viewBox="0 0 44 30"><path d="M10 28a8 8 0 0 1-1-16 12 12 0 0 1 23-2 9 9 0 0 1 2 18z" fill="none" stroke="#0e1f2f" stroke-width="2"/><path d="M16 11a6 6 0 0 1 7-4" fill="none" stroke="#fbb92c" stroke-width="2"/></svg>
    <div class="feature-body">
      <h3>Small Feature 1</h3>
      <p>Etiam ultricies nisi vel augue curabitur ullamcorper ultricies nisi nam eget dui etiam rhoncus maecenas tempus.</p>
      <a href="#">Read More</a>
    </div>
  </div>
  <div class="feature" style="left:344px">
    <svg width="40" height="28" viewBox="0 0 40 28"><rect x="4" y="2" width="32" height="19" fill="none" stroke="#0e1f2f" stroke-width="2.2"/><rect x="0" y="22" width="40" height="4" fill="#fbb92c"/></svg>
    <div class="feature-body">
      <h3>Small Feature 2</h3>
      <p>Etiam ultricies nisi vel augue curabitur ullamcorper ultricies nisi nam eget dui etiam rhoncus maecenas tempus.</p>
      <a href="#">Read More</a>
    </div>
  </div>
  <div class="feature" style="left:610px">
    <svg width="32" height="32" viewBox="0 0 32 32"><path d="M14 5L5 27 M7 27h19" stroke="#0e1f2f" stroke-width="1.3"/><circle cx="14" cy="5" r="3.5" fill="#fff" stroke="#fbb92c" stroke-width="1.5"/><circle cx="5" cy="27" r="3.5" fill="#fff" stroke="#fbb92c" stroke-width="1.5"/><circle cx="27" cy="26" r="3.5" fill="#fff" stroke="#fbb92c" stroke-width="1.5"/></svg>
    <div class="feature-body">
      <h3>Small Feature 3</h3>
      <p>Etiam ultricies nisi vel augue curabitur ullamcorper ultricies nisi nam eget dui etiam rhoncus maecenas tempus.</p>
      <a href="#">Read More</a>
    </div>
  </div>
  <div class="dots"><span class="on"></span><span></span></div>
</section>

<section class="newsletter">
  <div class="newsletter-label">Sign up to email newsletter</div>
  <div class="newsletter-field">Email address
    <svg width="10" height="6" viewBox="0 0 10 6"><path d="M0 3h9M6.5 .5L9 3 6.5 5.5" fill="none" stroke="#0e1f2f" stroke-width=".9"/></svg>
  </div>
  <div class="follow"><i></i>Follow &nbsp;@Vendlyx</div>
</section>

<footer class="site-footer">
  <div class="footer-brand">Vendlyx</div>
  <div class="social" aria-label="Social links"><span></span><span></span><span></span></div>
  <div class="copyright">© Vendlyx, All Rights Reserved.</div>
  <div class="legal"><a href="#">Terms &amp; Conditions</a><span>|</span><a href="#">Privacy Policy</a></div>
</footer>

</body>
</html>
```